依頼概要
■依頼目的/概要
Tolino(ブログ)内で「診断レポート」を提供しますので、
表紙デザイン作成をお願いいたします。

■納品物
下記での納品をお願いいたします。
JPEG形式
横1600ピクセル×縦2560ピクセル

■診断レポートの内容
<レポートのタイトル>
40代からのあなたの強みを最大限に生かすための3つの視点 ビジネスもプライベートも充実した人生を手に入れる

<キャッチコピー>
以下の文言の中から組み合わせるか、選んで載せてください。

・他人軸で生きる辛さから脱却しないと人生に悔いが残る!

・人生の転機のヒントが得られる!

・自分らしく生きるヒントが分かる!

・ハンディや持病を抱えながらも一部上場企業に貢献し、独立・起業したコーチが伝える

<著者名>
・著者名 前田芳典(ライフコーチ) M&R 合同会社 代表

■デザイン要望
・本のタイトル/キャッチコピー/著者名の反映をお願い致します。

・読者は40代50代60代の自分らしく生きようとしている人です。

・これからの人生設計を踏まえた考え方や捉え方を書いたレポートですので、
「ビジネス書の表紙」というイメージでお願いします。

・タイトル文字数が、ちょっと多いのですが、
できるだけ文字を認識しやすいようにしたいです。

・未来の人生に新たな可能性が見えるイメージです。

・タイトルの中では、「強み」「充実した人生」「生かす」
あたりが、目立つようにしたいです。

<表現したいイメージなど>
・信頼感
・ビジネス書っぽい感じ
・ベストセラーのマーケティング関連ビジネス書など、
どこかで見たことがあるような感じの安心感
・カラーの希望などはありません。お任せで。

<利用画像について>
イラスト等素材を使用される場合には、
商用利用可の素材をお願いします。

■その他、デザインを考えるのに必要な情報などありましたら、
お答えしますので、遠慮なく聞いて下さい。
■ 選んだ理由

皆様のレベルが高くて本当に嬉しい限りです。選定したポイントは、2案を出してもらいながら、シンプルで分かりやすく、タイトル周りの文字もメリハリがあり、「強み」「生かす」が強調されており、「人生の転機」も目を引き付けました。「充実した人生」も金色で表現しているところにデザインの秀逸さを感じました。また、ビジネス本という視点からも、青白でシンプルに構成され伝わりやすい表現がベストセラーにも多いので、そこにも共感をしました。一部修正依頼をさせていただいた対応も迅速丁寧で感謝しております。

■ 提案者全員のお礼・コメント

皆様、多くの素晴らしいご提案をいただき感謝しております。本当にありがとうございました。次回の依頼する際におきましてもご協力いただきますようお願いいたします。今後ともどうぞよろしくお願いいたします。

```html
<!DOCTYPE html>
<html lang="ja">
<head>
<meta charset="utf-8">
<title>40代からのあなたの強みを最大限に生かすための3つの視点</title>
<link href="https://fonts.googleapis.com/css2?family=Noto+Sans+JP:wght@500;700;900&display=swap" rel="stylesheet">
<style>
  :root {
    --navy: #1d3c78;
    --orange: #f0642a;
    --orange-soft: #f27744;
    --white: #ffffff;
  }
  * { margin: 0; padding: 0; box-sizing: border-box; }
  html, body { width: 750px; height: 1200px; overflow: hidden; background: var(--white); }
  body { font-family: "Noto Sans JP", sans-serif; color: var(--navy); }
  .cover { position: relative; width: 750px; height: 1200px; background: var(--white); overflow: hidden; }

  .tagline {
    position: absolute; top: 28px; left: 0; width: 100%;
    text-align: center; font-size: 23px; font-weight: 700; color: var(--navy);
    font-style: italic; letter-spacing: 0.02em;
  }
  .age-label {
    position: absolute; top: 86px; left: 225px; width: 300px; height: 60px;
    border: 4px solid var(--navy); border-radius: 16px;
    display: flex; align-items: center; justify-content: center;
    font-size: 40px; font-weight: 900; color: var(--navy);
  }
  .title-line {
    position: absolute; left: 0; width: 100%; text-align: center;
    font-weight: 900; color: var(--navy); line-height: 1; letter-spacing: -0.01em;
  }
  .title-line.first { top: 168px; font-size: 86px; }
  .title-line.second { top: 258px; font-size: 86px; }
  .title-line .accent { color: var(--orange); }
  .title-sub {
    position: absolute; top: 346px; left: 0; width: 100%;
    display: flex; justify-content: center; align-items: flex-end;
    font-weight: 900; color: var(--navy); line-height: 1;
  }
  .title-sub .small { font-size: 30px; margin-right: 8px; margin-bottom: 6px; }
  .title-sub .number { font-size: 100px; color: var(--orange); }
  .title-sub .rest { font-size: 74px; margin-bottom: 2px; }

  .band {
    position: absolute; top: 445px; left: 0; width: 750px; height: 340px;
    background: var(--orange);
  }
  .band-lead {
    position: absolute; top: 40px; left: 0; width: 100%; text-align: center;
    font-size: 48px; font-weight: 900; color: var(--white); line-height: 1;
  }
  .band-title {
    position: absolute; top: 115px; left: 0; width: 100%; text-align: center;
    font-size: 96px; font-weight: 900; color: var(--white); line-height: 1;
  }
  .band-tail {
    position: absolute; top: 262px; right: 60px;
    font-size: 46px; font-weight: 900; color: var(--navy); line-height: 1;
  }
  .band-art {
    position: absolute; top: 228px; left: 60px; width: 240px; height: 100px;
    background: linear-gradient(90deg, var(--orange), var(--orange-soft), var(--orange));
  }

  .catch {
    position: absolute; top: 878px; left: 400px;
    transform: rotate(-14deg); transform-origin: left top;
    font-size: 42px; font-weight: 900; color: var(--orange); line-height: 1.25;
    white-space: nowrap;
  }
  .catch .line2 { display: block; padding-left: 10px; }

  .bonus {
    position: absolute; top: 832px; left: 14px; width: 310px; height: 310px;
    border-radius: 50%; border: 10px solid var(--orange); background: var(--white);
    display: flex; flex-direction: column; align-items: center; justify-content: center;
    text-align: center; color: var(--navy); font-weight: 900;
  }
  .bonus-head { font-size: 44px; line-height: 1.1; }
  .bonus-limit {
    margin: 6px 0; padding: 2px 16px; background: var(--orange); color: var(--white);
    font-size: 22px; border-radius: 6px;
  }
  .bonus-body { font-size: 26px; line-height: 1.2; }
  .bonus-online { position: relative; font-size: 34px; line-height: 1.15; margin-top: 4px; padding: 0 26px; }
  .bonus-online .orange { color: var(--orange); display: block; }
  .bonus-online svg { position: absolute; top: 6px; height: 72px; width: 18px; }
  .bonus-online .left { left: 0; }
  .bonus-online .right { right: 0; }

  .author {
    position: absolute; right: 40px; top: 1016px; text-align: right;
    color: var(--navy); font-weight: 700;
  }
  .author-company { font-size: 28px; display: block; margin-right: 40px; margin-bottom: 18px; }
  .author-line { font-size: 28px; }
  .author-name { font-size: 44px; font-weight: 900; margin: 0 4px 0 10px; }
</style>
</head>
<body>
<main class="cover">
  <p class="tagline">ハンディや持病を抱えながらも、独立・起業したコーチが伝える</p>
  <div class="age-label">40代からの</div>
  <h1>
    <span class="title-line first">あなたの<span class="accent">強み</span>を</span>
    <span class="title-line second">最大限に<span class="accent">生かす</span></span>
    <span class="title-sub"><span class="small">ための</span><span class="number">3</span><span class="rest">つの視点</span></span>
  </h1>

  <section class="band">
    <p class="band-lead">ビジネスもプライベートも</p>
    <p class="band-title">充実した人生</p>
    <div class="band-art" role="img" aria-label="笑顔で並ぶ人々の線画イラスト"></div>
    <p class="band-tail">を手に入れる</p>
  </section>

  <p class="catch">他人軸で生きる<span class="line2">辛さからの脱却!</span></p>

  <aside class="bonus">
    <span class="bonus-head">読者特典</span>
    <span class="bonus-limit">人数限定</span>
    <span class="bonus-body">あなたの強みを<br>最大限に生かす</span>
    <span class="bonus-online">
      <svg class="left" viewBox="0 0 18 72"><polyline points="16,2 3,36 16,70" fill="none" stroke="#1d3c78" stroke-width="3"/></svg>
      <span class="orange">オンライン</span>セッション
      <svg class="right" viewBox="0 0 18 72"><polyline points="2,2 15,36 2,70" fill="none" stroke="#1d3c78" stroke-width="3"/></svg>
    </span>
  </aside>

  <footer class="author">
    <span class="author-company">M&amp;R合同会社　代表</span>
    <span class="author-line">ライフコーチ<span class="author-name">前田芳典</span>著</span>
  </footer>
</main>
</body>
</html>
```